Lumo App

We want to have a web banner (4-5 slides) flash or whatever.
We are innovative next generation messenger with a good design, themes, snap mode, pinging and other features.
Inspired by night, by techno music, by energy, by innovations and next generation.
High tech.

The name of the app : Quorlo
lumoapp.example

The banner will be used for nightlistings.example

We want the banner to be creative, and deliver the inspiration of the app.

All the assets, logos and so on can me delivered to you via email by request.

```html
<!DOCTYPE html>
<html lang="en">
<head>
<meta charset="utf-8">
<title>Quorlo App – Web Banner Slides</title>
<link rel="stylesheet" href="https://fonts.googleapis.com/css2?family=Montserrat:wght@300;400;700&display=swap">
<style>
  :root {
    --page-bg: #e4e4e4;
    --banner-black: #000000;
    --banner-dark: #1f1f1f;
    --banner-dark-2: #2b2b2b;
    --text-silver: #e9e9e9;
    --text-white: #ffffff;
    --accent-blue: #1c8fdc;
    --accent-green: #8fc31f;
    --badge-bg: #050505;
    --badge-border: #8a8a8a;
    --mark-blue: #5ab8f0;
    --shadow: rgba(0, 0, 0, 0.45);
  }

  * { margin: 0; padding: 0; box-sizing: border-box; }

  html, body {
    width: 1200px;
    height: 830px;
    overflow: hidden;
  }

  body {
    background: var(--page-bg);
    font-family: "Montserrat", Arial, sans-serif;
    position: relative;
  }

  .banner {
    position: absolute;
    left: 118px;
    width: 961px;
    height: 119px;
    overflow: hidden;
    background: var(--banner-black);
    box-shadow: 8px 10px 12px var(--shadow);
  }

  .banner--night   { top: 90px; }
  .banner--mobile  { top: 272px; }
  .banner--now     { top: 455px; }
  .banner--store   { top: 637px; background: linear-gradient(180deg, var(--banner-dark-2), var(--banner-dark)); }

  .photo {
    position: absolute;
    top: 0;
    height: 100%;
  }

  .photo--lasers {
    left: 318px;
    right: 0;
    background:
      linear-gradient(90deg, var(--banner-black) 0%, rgba(0,0,0,0) 22%),
      radial-gradient(ellipse at 55% 20%, rgba(120, 220, 60, 0.55), rgba(0,0,0,0) 55%),
      linear-gradient(180deg, #1a2a1a 0%, #2a1f48 55%, #0a0a12 100%);
  }

  .photo--city {
    left: 340px;
    right: 0;
    background:
      linear-gradient(90deg, var(--banner-black) 0%, rgba(0,0,0,0) 20%),
      radial-gradient(ellipse at 40% 75%, rgba(70, 110, 170, 0.35), rgba(0,0,0,0) 55%),
      linear-gradient(180deg, #1f2633 0%, #161d2b 50%, #0b0e16 100%);
  }

  .photo--crowd {
    left: 0;
    width: 600px;
    background:
      linear-gradient(270deg, var(--banner-black) 0%, rgba(0,0,0,0) 30%),
      radial-gradient(ellipse at 25% 20%, rgba(90, 200, 80, 0.6), rgba(0,0,0,0) 50%),
      radial-gradient(ellipse at 60% 25%, rgba(220, 150, 70, 0.45), rgba(0,0,0,0) 45%),
      linear-gradient(180deg, #2a2a3a 0%, #15131c 70%, #050505 100%);
  }

  .photo--phones {
    left: 83px;
    top: 11px;
    width: 195px;
    height: 108px;
    border-radius: 14px 14px 0 0;
    background: linear-gradient(180deg, #3a3a3a 0%, #1e1e1e 100%);
  }

  .headline {
    position: absolute;
    font-weight: 300;
    white-space: nowrap;
    line-height: 1;
  }

  .headline--night {
    left: 19px;
    top: 34px;
    font-size: 49px;
    color: var(--text-silver);
  }

  .headline--messenger {
    left: 24px;
    top: 20px;
    font-size: 31px;
    color: var(--text-white);
  }

  .headline--mobile {
    left: 25px;
    top: 69px;
    font-size: 32px;
    color: var(--accent-blue);
  }

  .headline--now {
    right: 35px;
    top: 40px;
    font-size: 45px;
    color: var(--accent-green);
  }

  .brand__square {
    position: absolute;
    left: 324px;
    top: 36px;
    width: 52px;
    height: 52px;
    background: var(--mark-blue);
    border: 2px solid var(--text-white);
  }

  .brand__name {
    position: absolute;
    left: 392px;
    top: 42px;
    font-size: 34px;
    font-weight: 700;
    line-height: 1;
    color: var(--text-white);
  }

  .store-badge {
    position: absolute;
    top: 43px;
    width: 173px;
    height: 51px;
    background: var(--badge-bg);
    border: 1px solid var(--badge-border);
    border-radius: 7px;
  }

  .store-badge--first  { left: 567px; }
  .store-badge--second { left: 758px; }
</style>
</head>
<body>

  <section class="banner banner--night" aria-label="Slide 1">
    <div class="photo photo--lasers" role="img" aria-label="Night club stage with green laser beams over a crowd"></div>
    <h1 class="headline headline--night">INSPIRED BY NIGHT!</h1>
  </section>

  <section class="banner banner--mobile" aria-label="Slide 2">
    <div class="photo photo--city" role="img" aria-label="City skyline at night seen from a rooftop"></div>
    <p class="headline headline--messenger">NEXT GENERATION MESSENGER</p>
    <p class="headline headline--mobile">FOR YOUR MOBILE</p>
  </section>

  <section class="banner banner--now" aria-label="Slide 3">
    <div class="photo photo--crowd" role="img" aria-label="Dancing crowd under colourful club lights"></div>
    <p class="headline headline--now">AVAILABLE NOW</p>
  </section>

  <section class="banner banner--store" aria-label="Slide 4">
    <div class="photo photo--phones" role="img" aria-label="Two smartphones showing the Quorlo chat screen"></div>
    <span class="brand__square"></span>
    <span class="brand__name">Quorlo</span>
    <span class="store-badge store-badge--first" aria-label="App store download badge"></span>
    <span class="store-badge store-badge--second" aria-label="App store download badge"></span>
  </section>

</body>
</html>
```